Tallmark Benefit Advisors Business Card Design

I already placed order for cards through press grove.

Double sided- back Navy with White logo and raised silver "swoosh"

```html
<!DOCTYPE html>
<html lang="en">
<head>
<meta charset="utf-8">
<title>Tallmark Benefit Advisors — Business Card</title>
<link rel="stylesheet" href="https://fonts.googleapis.com/css2?family=Tinos:wght@400;700&display=swap">
<style>
  :root {
    --backdrop: #ecebea;
    --paper: #f7f7f6;
    --navy: #0f2350;
    --navy-deep: #0a1c45;
    --ink-grey: #555555;
    --rule-grey: #8a8a8a;
    --white: #ffffff;
  }
  * { margin: 0; padding: 0; box-sizing: border-box; }
  html, body {
    width: 1200px;
    height: 801px;
    overflow: hidden;
    background: var(--backdrop);
    font-family: "Tinos", "Times New Roman", serif;
  }
  .sheet {
    width: 1200px;
    height: 801px;
    display: flex;
    align-items: center;
    justify-content: center;
    gap: 48px;
  }
  .card {
    width: 540px;
    height: 309px;
    position: relative;
    box-shadow: 0 6px 18px rgba(0,0,0,0.14);
  }
  .card--front { background: var(--paper); }
  .card--back {
    background: var(--navy);
    display: flex;
    align-items: center;
    justify-content: center;
  }
  .brand {
    display: flex;
    align-items: center;
    gap: 10px;
  }
  .brand__dot {
    width: 12px;
    height: 12px;
    border-radius: 50%;
    flex: none;
  }
  .brand__name {
    font-weight: 400;
    text-transform: uppercase;
    letter-spacing: 0.06em;
    line-height: 1.15;
  }
  .card--front .brand {
    position: absolute;
    left: 34px;
    top: 138px;
    width: 220px;
  }
  .card--front .brand__dot { background: var(--navy); }
  .card--front .brand__name { color: var(--navy); font-size: 17px; }
  .card--back .brand__dot { background: var(--white); width: 18px; height: 18px; }
  .card--back .brand__name { color: var(--white); font-size: 30px; }
  .divider {
    position: absolute;
    left: 270px;
    top: 64px;
    width: 1px;
    height: 186px;
    background: var(--rule-grey);
  }
  .contact {
    position: absolute;
    left: 292px;
    top: 62px;
    color: var(--ink-grey);
    font-size: 15px;
    line-height: 1.3;
  }
  .contact__name {
    color: var(--navy);
    font-weight: 700;
    font-size: 17px;
    letter-spacing: 0.02em;
    text-transform: uppercase;
  }
  .contact__role { margin-bottom: 12px; }
  .contact__address { margin-bottom: 12px; }
  .contact__row {
    display: flex;
    align-items: center;
    gap: 7px;
  }
  .contact__icon { width: 13px; height: 13px; flex: none; }
</style>
</head>
<body>
<main class="sheet">
  <section class="card card--front" aria-label="Card front">
    <div class="brand">
      <span class="brand__dot"></span>
      <span class="brand__name">Tallmark Benefit Advisors</span>
    </div>
    <div class="divider"></div>
    <div class="contact">
      <p class="contact__name">Daniel Hart</p>
      <p class="contact__role">Managing Director</p>
      <p class="contact__address">Your Address, City<br>State, Zip 0000</p>
      <p class="contact__row">
        <svg class="contact__icon" viewBox="0 0 16 16" aria-hidden="true"><circle cx="8" cy="8" r="8" fill="#0f2350"/><path d="M5 4.5c.6-.5 1.2-.3 1.5.3l.5 1c.2.4 0 .8-.3 1l-.4.3c.4.9 1.1 1.6 2 2l.3-.4c.3-.3.7-.4 1-.2l1 .5c.6.3.8.9.3 1.5-.7.8-1.8.9-2.8.3-1.5-.8-2.6-2-3.4-3.4-.5-1-.5-2.1.3-2.9z" fill="#fff"/></svg>
        044-123 456 789
      </p>
      <p class="contact__row">
        <svg class="contact__icon" viewBox="0 0 16 16" aria-hidden="true"><circle cx="8" cy="8" r="8" fill="#0f2350"/><rect x="4" y="5.2" width="8" height="5.6" fill="#fff"/><path d="M4 5.2l4 3 4-3" stroke="#0f2350" stroke-width="0.9" fill="none"/></svg>
        info@webname.com
      </p>
      <p class="contact__row">
        <svg class="contact__icon" viewBox="0 0 16 16" aria-hidden="true"><circle cx="8" cy="8" r="8" fill="#0f2350"/><circle cx="8" cy="8" r="4.2" fill="none" stroke="#fff" stroke-width="1"/><path d="M3.8 8h8.4M8 3.8c-1.6 2.4-1.6 6 0 8.4M8 3.8c1.6 2.4 1.6 6 0 8.4" stroke="#fff" stroke-width="0.8" fill="none"/></svg>
        www.websitename.com
      </p>
    </div>
  </section>

  <section class="card card--back" aria-label="Card back">
    <div class="brand">
      <span class="brand__dot"></span>
      <span class="brand__name">Tallmark Benefit Advisors</span>
    </div>
  </section>
</main>
</body>
</html>
```